Real Estate Team Needs Business Cards

Double sided - Team Member on Front, Team Leader on Back (back side will contain more details).
Colors to use:
Red = R: 233 G: 1 B: 2
Grey = R: 89 G: 89 B: 89
Black= R: 0 B: 0 B: 0
** MAIN FOCUS ** ( separate border, color, design, etc. to really stand out - whatever you think draws the most attention ) on both sides for "Sell for 1%‡" and "Buy & receive up to a 1% rebate‡". Must have fine print **
**Please make both sides stand out and look unique / different
Business card to have round corners (standard size 3.5" x 2").:
Document Trim Size
89 x 51 mm
1050 x 600 pixels
Full Bleed Size
92 x 54 mm
1085 x 635 pixels
Basic example provided. Please redesign as you see best. In your design - Please use the same picture on both sides. Name, address, phone number, email, etc. will be provided to the selected design. QR code on back side only if there is room (not important)

```html
<!DOCTYPE html>
<html lang="en">
<head>
<meta charset="utf-8">
<title>Summit Key Realty – Business Cards</title>
<link href="https://fonts.googleapis.com/css2?family=Roboto:wght@400;500;700;900&display=swap" rel="stylesheet">
<style>
  :root {
    --red: rgb(233, 1, 2);
    --grey: rgb(89, 89, 89);
    --black: #000;
    --white: #fff;
    --backdrop: #e6e7e9;
    --suit-navy: #23386b;
    --shirt: #dfe6ef;
  }
  * { box-sizing: border-box; margin: 0; padding: 0; }
  html, body { width: 1200px; height: 913px; overflow: hidden; }
  body {
    background: var(--backdrop);
    font-family: "Roboto", Arial, sans-serif;
    position: relative;
  }
  .card {
    position: absolute;
    width: 640px;
    height: 366px;
    background: var(--white);
    border-radius: 14px;
    overflow: hidden;
    box-shadow: 0 6px 18px rgba(0,0,0,0.18);
  }
  .card--front { left: 40px; top: 40px; }
  .card--back  { left: 520px; top: 500px; }

  .brand {
    position: absolute;
    display: flex;
    align-items: center;
    gap: 10px;
    font-weight: 900;
    letter-spacing: 0.5px;
    color: var(--black);
    text-transform: uppercase;
    white-space: nowrap;
  }
  .brand__square { width: 16px; height: 16px; background: var(--red); flex: none; }
  .card--front .brand { left: 290px; top: 52px; font-size: 30px; }
  .card--back  .brand { right: 24px; top: 44px; font-size: 23px; }
  .card--back  .brand__square { width: 13px; height: 13px; }

  .offer-band {
    position: absolute;
    left: 0; right: 0;
    background: var(--red);
  }
  .card--front .offer-band { top: 140px; height: 86px; }
  .card--back  .offer-band { top: 120px; height: 84px; }

  .offer {
    position: absolute;
    color: var(--white);
    font-weight: 500;
    text-transform: uppercase;
    line-height: 1.35;
    letter-spacing: 0.3px;
    white-space: nowrap;
  }
  .card--front .offer { left: 256px; top: 154px; font-size: 21px; }
  .card--back  .offer { left: 274px; top: 135px; font-size: 20px; }

  .portrait {
    position: absolute;
    background: linear-gradient(180deg, #d9b8a3 0%, #cfa890 30%, var(--shirt) 42%, var(--suit-navy) 55%, #1c2f5c 100%);
    border-radius: 90px 90px 0 0;
  }
  .card--front .portrait { left: 40px; top: 70px; width: 200px; height: 296px; }
  .card--back  .portrait { left: 100px; top: 140px; width: 160px; height: 226px; }

  .services {
    position: absolute;
    left: 290px; top: 244px;
    list-style: none;
    font-size: 17px;
    font-weight: 500;
    color: var(--black);
    line-height: 1.45;
  }
  .services li { display: flex; align-items: center; gap: 10px; }
  .services li::before {
    content: ""; width: 9px; height: 9px; background: var(--red); flex: none;
  }
  .front-web {
    position: absolute;
    left: 290px; top: 324px;
    color: var(--red);
    font-weight: 700;
    font-size: 18px;
    letter-spacing: 0.3px;
    white-space: nowrap;
  }

  .agent { position: absolute; left: 28px; top: 40px; white-space: nowrap; }
  .agent__name {
    color: var(--red);
    font-size: 26px;
    font-weight: 500;
    text-transform: uppercase;
    letter-spacing: 0.5px;
  }
  .agent__role { font-size: 17px; color: var(--black); letter-spacing: 1px; margin-top: 4px; }

  .contacts {
    position: absolute;
    right: 22px; top: 218px;
    list-style: none;
    text-align: right;
    font-size: 17px;
    color: var(--black);
    line-height: 1.42;
    white-space: nowrap;
  }
  .contacts li { display: flex; justify-content: flex-end; align-items: center; gap: 10px; }
  .contacts svg { width: 15px; height: 15px; fill: var(--red); flex: none; }
  .contacts .accent { color: var(--red); }
</style>
</head>
<body>

  <section class="card card--front" aria-label="Business card front">
    <div class="offer-band"></div>
    <div class="brand"><span class="brand__square"></span>Summit Key Realty</div>
    <div class="portrait" role="img" aria-label="Portrait photo of the agent in a navy suit and light blue tie"></div>
    <p class="offer">Sell for 1%*<br>Buy &amp; receive up to a 1% rebate*</p>
    <ul class="services">
      <li>Free Home Evaluation</li>
      <li>Free Local Sold Reports</li>
      <li>Advanced Property Search</li>
    </ul>
    <p class="front-web">WWW.SUMMITKEYREALTY.COM</p>
  </section>

  <section class="card card--back" aria-label="Business card back">
    <div class="offer-band"></div>
    <div class="agent">
      <p class="agent__name">Daniel Whitcombe</p>
      <p class="agent__role">Director</p>
    </div>
    <div class="brand"><span class="brand__square"></span>Summit Key Realty</div>
    <div class="portrait" role="img" aria-label="Portrait photo of the team leader in a navy suit and light blue tie"></div>
    <p class="offer">Sell for 1%*<br>Buy &amp; receive up to a 1% rebate*</p>
    <ul class="contacts">
      <li>01 555 01234
        <svg viewBox="0 0 24 24"><path d="M6.6 10.8a15 15 0 0 0 6.6 6.6l2.2-2.2a1 1 0 0 1 1-.25 11.4 11.4 0 0 0 3.6.57 1 1 0 0 1 1 1V20a1 1 0 0 1-1 1A17 17 0 0 1 3 4a1 1 0 0 1 1-1h3.5a1 1 0 0 1 1 1c0 1.25.2 2.45.57 3.6a1 1 0 0 1-.25 1z"/></svg></li>
      <li>01 555 01234
        <svg viewBox="0 0 24 24"><path d="M7 1h10a2 2 0 0 1 2 2v18a2 2 0 0 1-2 2H7a2 2 0 0 1-2-2V3a2 2 0 0 1 2-2zm0 3v15h10V4zm5 16.2a1 1 0 1 0 0 .1z"/></svg></li>
      <li>info@summitkeyrealty.com
        <svg viewBox="0 0 24 24"><path d="M2 5h20v14H2zm2 2v.5l8 5 8-5V7l-8 5z"/></svg></li>
      <li><span>www.<span class="accent">summitkeyrealty</span>.com</span>
        <svg viewBox="0 0 24 24"><path d="M12 2a10 10 0 1 0 0 20 10 10 0 0 0 0-20zm0 2c1 0 2.3 2 2.8 5H9.2C9.7 6 11 4 12 4zM4.3 11h4.6a18 18 0 0 0 0 2H4.3a8 8 0 0 1 0-2zm10.8 0h4.6a8 8 0 0 1 0 2h-4.6a18 18 0 0 0 0-2zM9.2 15h5.6c-.5 3-1.8 5-2.8 5s-2.3-2-2.8-5z"/></svg></li>
      <li>42 Maple Lane, Suite 210, NJ
        <svg viewBox="0 0 24 24"><path d="M12 2a7 7 0 0 0-7 7c0 5 7 13 7 13s7-8 7-13a7 7 0 0 0-7-7zm0 9.5A2.5 2.5 0 1 1 12 6.5a2.5 2.5 0 0 1 0 5z"/></svg></li>
    </ul>
  </section>

</body>
</html>
```